New Infographic Design Project

Hi, I have another project to work on if you are interested. It is a horizontal style infographic with 6 steps. It should display the step Number (1-6), Title, and an Icon.

Step 1 - Strong Phone Interview
Step 2 - Pre-Employment
Step 3 - Prep & Do In-Person Interview
Step 4 - Second Interview
Step 5 - Reference Checks
Step 6 - Job Offer

More flexible on colors with this one, but keep it professional.

```html
<!DOCTYPE html>
<html lang="en">
<head>
<meta charset="UTF-8">
<title>Hiring Process in Six Steps</title>
<link href="https://fonts.googleapis.com/css2?family=Montserrat:wght@600;700&display=swap" rel="stylesheet">
<style>
  :root {
    --page: #ffffff;
    --ink: #111111;
    --blob: #d9deee;
    --icon: #000000;
    --icon-cut: #ffffff;
  }
  * { margin: 0; padding: 0; box-sizing: border-box; }
  html, body {
    width: 1200px;
    height: 674px;
    overflow: hidden;
    background: var(--page);
  }
  body {
    font-family: "Montserrat", Arial, sans-serif;
    color: var(--ink);
  }
  .process {
    width: 1200px;
    height: 674px;
    padding: 0 12px;
    display: grid;
    grid-template-columns: repeat(6, 1fr);
    align-items: start;
  }
  .step {
    display: flex;
    flex-direction: column;
    align-items: center;
    text-align: center;
  }
  .step-number {
    margin-top: 150px;
    font-size: 21px;
    font-weight: 700;
    letter-spacing: 0.2px;
  }
  .step-icon {
    margin-top: 58px;
    width: 176px;
    height: 176px;
    display: block;
  }
  .step-title {
    margin-top: 58px;
    height: 48px;
    display: flex;
    align-items: center;
    justify-content: center;
    font-size: 17.5px;
    font-weight: 700;
    line-height: 1.15;
    max-width: 180px;
  }
  .blob { fill: var(--blob); }
  .icon { fill: var(--icon); }
  .icon-light { fill: var(--icon-cut); }
  .icon-cut { fill: none; stroke: var(--icon-cut); stroke-width: 4; stroke-linecap: round; stroke-linejoin: round; }
  .icon-line { fill: none; stroke: var(--icon); stroke-width: 4; stroke-linecap: round; stroke-linejoin: round; }
</style>
</head>
<body>
<main class="process">

  <section class="step">
    <h2 class="step-number">Step 1</h2>
    <svg class="step-icon" viewBox="0 0 200 200" aria-hidden="true">
      <path class="blob" d="M100 18 C140 10 178 40 176 78 C174 110 196 130 180 160 C162 192 120 186 95 188 C60 190 22 176 20 140 C18 108 8 80 30 50 C48 26 72 22 100 18Z"/>
      <circle class="icon" cx="132" cy="66" r="34"/>
      <path class="icon" d="M108 88 L100 112 L124 96 Z"/>
      <circle class="icon-light" cx="132" cy="54" r="9"/>
      <rect class="icon-light" x="120" y="66" width="24" height="20" rx="5"/>
      <g transform="translate(30 62) scale(4.6)">
        <path class="icon" d="M6.62 10.79c1.44 2.830 3.76 5.14 6.59 6.59l2.2-2.2c.27-.27.67-.36 1.02-.24 1.12.37 2.33.57 3.57.57.55 0 1 .45 1 1V20c0 .55-.45 1-1 1-9.39 0-17-7.61-17-17 0-.55.45-1 1-1h3.5c.55 0 1 .45 1 1 0 1.25.2 2.45.57 3.57.11.35.03.74-.25 1.02l-2.2 2.2z"/>
      </g>
    </svg>
    <p class="step-title">Strong Phone Interview</p>
  </section>

  <section class="step">
    <h2 class="step-number">Step 2</h2>
    <svg class="step-icon" viewBox="0 0 200 200" aria-hidden="true">
      <path class="blob" transform="rotate(20 100 100)" d="M100 18 C140 10 178 40 176 78 C174 110 196 130 180 160 C162 192 120 186 95 188 C60 190 22 176 20 140 C18 108 8 80 30 50 C48 26 72 22 100 18Z"/>
      <path class="icon" d="M58 40 H124 L146 62 V164 H58 Z"/>
      <path class="icon-light" d="M124 40 V62 H146 Z" opacity="0.35"/>
      <rect class="icon-cut" x="72" y="74" width="12" height="12" stroke-width="3"/>
      <path class="icon-cut" d="M74 80 l3 3 l6 -7" stroke-width="3"/>
      <path class="icon-cut" d="M94 80 H132"/>
      <rect class="icon-cut" x="72" y="100" width="12" height="12" stroke-width="3"/>
      <path class="icon-cut" d="M94 106 H132"/>
      <rect class="icon-cut" x="72" y="126" width="12" height="12" stroke-width="3"/>
      <path class="icon-cut" d="M94 132 H132"/>
    </svg>
    <p class="step-title">Pre-Employment</p>
  </section>

  <section class="step">
    <h2 class="step-number">Step 3</h2>
    <svg class="step-icon" viewBox="0 0 200 200" aria-hidden="true">
      <path class="blob" transform="translate(200 0) scale(-1 1)" d="M100 18 C140 10 178 40 176 78 C174 110 196 130 180 160 C162 192 120 186 95 188 C60 190 22 176 20 140 C18 108 8 80 30 50 C48 26 72 22 100 18Z"/>
      <rect class="icon" x="44" y="56" width="112" height="76" rx="6"/>
      <rect class="icon-light" x="52" y="64" width="96" height="58" opacity="0.2"/>
      <path class="icon" d="M90 132 H110 L114 152 H86 Z"/>
      <rect class="icon" x="70" y="152" width="60" height="8" rx="3"/>
    </svg>
    <p class="step-title">Prep Do In-Person Interview</p>
  </section>

  <section class="step">
    <h2 class="step-number">Step 4</h2>
    <svg class="step-icon" viewBox="0 0 200 200" aria-hidden="true">
      <path class="blob" transform="rotate(-15 100 100)" d="M100 18 C140 10 178 40 176 78 C174 110 196 130 180 160 C162 192 120 186 95 188 C60 190 22 176 20 140 C18 108 8 80 30 50 C48 26 72 22 100 18Z"/>
      <rect class="icon" x="40" y="52" width="80" height="54" rx="10"/>
      <path class="icon" d="M56 104 L52 124 L74 104 Z"/>
      <path class="icon-cut" d="M54 72 H106 M54 86 H90"/>
      <rect class="icon" x="88" y="96" width="74" height="50" rx="10"/>
      <path class="icon" d="M146 144 L150 162 L130 144 Z"/>
      <circle class="icon-light" cx="108" cy="121" r="4"/>
      <circle class="icon-light" cx="125" cy="121" r="4"/>
      <circle class="icon-light" cx="142" cy="121" r="4"/>
    </svg>
    <p class="step-title">Second Interview</p>
  </section>

  <section class="step">
    <h2 class="step-number">Step 5</h2>
    <svg class="step-icon" viewBox="0 0 200 200" aria-hidden="true">
      <path class="blob" transform="translate(0 200) scale(1 -1)" d="M100 18 C140 10 178 40 176 78 C174 110 196 130 180 160 C162 192 120 186 95 188 C60 190 22 176 20 140 C18 108 8 80 30 50 C48 26 72 22 100 18Z"/>
      <rect class="icon" x="58" y="44" width="86" height="118"/>
      <path class="icon-cut" d="M86 46 h30" stroke-width="3"/>
      <rect class="icon" x="88" y="36" width="26" height="10" rx="2"/>
      <circle class="icon-cut" cx="101" cy="104" r="22"/>
      <path class="icon-cut" d="M91 104 l7 7 l13 -13"/>
    </svg>
    <p class="step-title">Reference Checks</p>
  </section>

  <section class="step">
    <h2 class="step-number">Step 6</h2>
    <svg class="step-icon" viewBox="0 0 200 200" aria-hidden="true">
      <path class="blob" transform="rotate(40 100 100)" d="M100 18 C140 10 178 40 176 78 C174 110 196 130 180 160 C162 192 120 186 95 188 C60 190 22 176 20 140 C18 108 8 80 30 50 C48 26 72 22 100 18Z"/>
      <path class="icon-line" d="M84 66 V54 H116 V66" stroke-width="7"/>
      <rect class="icon" x="46" y="64" width="108" height="76" rx="6"/>
      <path class="icon-cut" d="M46 96 H154" stroke-width="3"/>
      <rect class="icon-light" x="90" y="88" width="20" height="14" rx="2"/>
      <rect class="icon" x="40" y="150" width="120" height="10" rx="5"/>
    </svg>
    <p class="step-title">Job Offer</p>
  </section>

</main>
</body>
</html>
```